依頼詳細
引越を考えているお客様にチラシを渡して頂くため、不動産店舗を回って交渉をしています。
その際に営業の皆様に渡す名刺です。
「引越業者選び面倒臭い!とお思いの皆様へ。」
「数多くある引越業者から安くしっかりした業者を選定してくれる」「面倒なことを全て引き受けてくれる」ことが売りの会社です。

チラシはお客様向けなのでポップな雰囲気で分かり易く作って頂いていますが、名刺のデザインとしては
信頼感や堅実さを押し出すのが良いのかなと思っています。

添付のファイルは会社のロゴです。

それでは宜しくお願いいたします。
記載項目
株式会社brightway/役職名/佐藤 健一/KENICHI SATO/本社所在地 〒105-0021 東京都港区東新橋4-2-8/代表 03-5417-3861/お見積専用ダイヤル0120-583-216/HP www.bwaymv.co.jp/Mail info.bwaymv.co.jp/
希望イメージ
シンプル 複雑
単色 カラフル
暗い 明るい
日常 高級
遊び心 厳粛
未来的 伝統的
女性的 男性的
希望する色
納品ファイル
• 高解像度JPG (.jpg)
• イラストレーター形式 (.ai)
補足説明
添付しましたイラストレーターファイル(会社ロゴ)につきまして、バージョンが新しいために開けない、古く出来ないかとのご相談がありました。
取り急ぎ、解像度が粗いですがjpgファイルを添付しますので、仮でこれをお使い下さい。

どれを使ってあっても、全体のデザインが気に入れば採用します。
■ 選んだ理由

お伝えしたかった意図をよく汲んで頂いたこと、見た目の爽やかさと分かりやすさが決め手となりました。
こちらからの要望も気持ち良く受けて頂き、感謝しています。

■ 提案者全員のお礼・コメント

とても素晴らしいご提案を沢山頂きました。
惜しくも選外とさせて頂いた方も、また別の機会にお付き合い頂ければ幸いです。

```html
<!DOCTYPE html>
<html lang="ja">
<head>
<meta charset="utf-8">
<title>佐藤 健一 名刺 — 株式会社brightway</title>
<link rel="stylesheet" href="https://fonts.googleapis.com/css2?family=Noto+Serif+JP:wght@400;500&display=swap">
<style>
  :root {
    --paper: #ffffff;
    --ink: #1a1a1a;
    --brand-green: #8cc63e;
    --brand-blue: #4aa6d8;
    --accent-orange: #f29a2e;
  }
  html, body { margin: 0; padding: 0; overflow: hidden; background: var(--paper); }
  .card {
    position: relative;
    width: 726px;
    height: 1200px;
    background: var(--paper);
    color: var(--ink);
    font-family: "Noto Serif JP", serif;
    overflow: hidden;
  }
  .brand {
    position: absolute;
    left: 245px;
    top: 98px;
    display: flex;
    align-items: center;
    gap: 24px;
  }
  .brand-square {
    width: 100px;
    height: 100px;
    background: var(--brand-blue);
  }
  .brand-name {
    font-size: 44px;
    font-weight: 400;
    color: var(--ink);
    line-height: 1.15;
    text-align: right;
  }
  .brand-name span { display: block; }
  .vertical { position: absolute; writing-mode: vertical-rl; }
  .job-title { left: 205px; top: 218px; font-size: 32px; letter-spacing: 0.08em; }
  .person-name { left: 78px; top: 282px; font-size: 80px; font-weight: 400; letter-spacing: 0.06em; line-height: 1; }
  .person-roman { left: 92px; top: 775px; font-size: 27px; letter-spacing: 0.06em; }
  .company {
    position: absolute; left: 250px; top: 805px;
    font-size: 34px; letter-spacing: 0.02em; margin: 0; font-weight: 400;
  }
  .contact {
    position: absolute; left: 250px; top: 935px;
    margin: 0; padding: 0; list-style: none;
    font-size: 28px; line-height: 40px;
  }
  .contact li { display: flex; align-items: center; gap: 8px; white-space: nowrap; }
  .contact svg { width: 28px; height: 28px; flex: none; }
</style>
</head>
<body>
<div class="card">
  <div class="brand">
    <div class="brand-square"></div>
    <div class="brand-name"><span>brightway</span><span>Co.,Ltd</span></div>
  </div>

  <div class="vertical job-title">代表取締役</div>
  <div class="vertical person-name">佐藤　健一</div>
  <div class="vertical person-roman">KENICHI SATO</div>

  <h1 class="company">株式会社 brightway</h1>
  <ul class="contact">
    <li>〒105-0021</li>
    <li>東京都港区東新橋4-2-8</li>
    <li>
      <svg viewBox="0 0 30 30" aria-hidden="true"><path fill="var(--brand-green)" d="M8 4c1-1 2-1 3 0l3 4c.6 1 .4 2-.4 2.8l-1.6 1.4c1.2 2.6 3.2 4.6 5.8 5.8l1.4-1.6c.8-.8 1.8-1 2.8-.4l4 3c1 1 1 2 0 3l-2 2c-1.5 1.5-4 1.5-7-.3C12 21 9 18 6.3 13 4.5 10 4.5 7.5 6 6z"/></svg>
      03-5417-3861(代表)
    </li>
    <li>
      <svg viewBox="0 0 30 30" aria-hidden="true"><rect x="1" y="7" width="28" height="16" rx="8" fill="var(--accent-orange)"/><circle cx="10" cy="15" r="4" fill="var(--paper)"/><circle cx="20" cy="15" r="4" fill="var(--paper)"/></svg>
      0120-583-216(お見積専用)
    </li>
    <li>
      <svg viewBox="0 0 30 30" aria-hidden="true"><circle cx="15" cy="15" r="12" fill="var(--brand-green)"/><g fill="none" stroke="var(--paper)" stroke-width="1.6"><ellipse cx="15" cy="15" rx="5" ry="12"/><line x1="3" y1="15" x2="27" y2="15"/><line x1="15" y1="3" x2="15" y2="27"/></g></svg>
      www.bwaymv.co.jp
    </li>
    <li>
      <svg viewBox="0 0 30 30" aria-hidden="true"><rect x="2" y="6" width="26" height="18" fill="var(--brand-green)"/><polyline points="2,6 15,17 28,6" fill="none" stroke="var(--paper)" stroke-width="2"/></svg>
      info.bwaymv.co.jp/
    </li>
  </ul>
</div>
</body>
</html>
```